RTV Business Card

We need a new design for our business cards. We are brokers in the scrap metal industry and wants something nice, clean and very professional.

Industry/Entity Type

Business

Requirements
Must have
• Our logo
• Would probably be good to incorporate colors from logo into design.
• Example info we need on the cards.
• Name
• Company Address
• Cell Phone
• Office Phone
• Fax
• Email
• Company Website
Should not have
• Should not be too cluttered. Needs to be nice, clean and professional looking.

```html
<!DOCTYPE html>
<html lang="en">
<head>
<meta charset="utf-8">
<title>RTV Business Card</title>
<link href="https://fonts.googleapis.com/css2?family=Source+Sans+3:wght@700&family=Arimo:wght@400&display=swap" rel="stylesheet">
<style>
  :root {
    --bg: #1c1c1c;
    --card: #ffffff;
    --navy: #0d3f78;
    --blue: #1a73b8;
    --red: #e0222b;
    --ink: #111111;
    --grey: #555555;
    --body: #333333;
  }
  * { margin: 0; padding: 0; box-sizing: border-box; }
  html, body { width: 1200px; height: 900px; overflow: hidden; background: var(--bg); }
  .stage { position: relative; width: 1200px; height: 900px; }

  .card {
    position: absolute;
    width: 700px; height: 400px;
    background: var(--card);
    overflow: hidden;
    box-shadow: 0 10px 30px rgba(0,0,0,.6);
  }
  .card--front { left: 60px; top: 40px; }
  .card--back  { left: 440px; top: 470px; }

  /* Front */
  .front-panel {
    position: absolute; left: 0; bottom: 0;
    width: 300px; height: 210px;
    background: linear-gradient(135deg, var(--blue), var(--navy));
    clip-path: polygon(0 0, 70% 0, 100% 100%, 0 100%);
  }
  .front-band-red {
    position: absolute; left: 300px; bottom: 0;
    width: 250px; height: 10px; background: var(--red);
  }
  .front-band-blue {
    position: absolute; left: 550px; bottom: 0;
    width: 150px; height: 10px; background: var(--navy);
  }
  .front-edge {
    position: absolute; right: 0; top: 0;
    width: 10px; height: 400px; background: var(--navy);
  }
  .front-brand {
    position: absolute; left: 300px; top: 130px;
    text-align: right; width: 360px;
  }
  .company {
    font-family: "Source Sans 3", sans-serif;
    font-weight: 700; color: var(--ink);
    letter-spacing: -0.5px;
    white-space: nowrap;
  }
  .front-brand .company { font-size: 36px; }
  .website-line {
    font-family: "Arimo", sans-serif;
    font-size: 13px; letter-spacing: 3px; color: var(--grey);
    margin-top: 2px;
  }
  .website-line .accent { color: var(--red); }

  /* Back */
  .side-bar { position: absolute; left: 0; top: 0; width: 22px; height: 400px; }
  .side-bar span { display: block; width: 100%; }
  .side-bar .seg-blue-top { height: 130px; background: var(--blue); }
  .side-bar .seg-red { height: 120px; background: var(--red); }
  .side-bar .seg-blue-bottom { height: 150px; background: var(--navy); }

  .back-panel-blue {
    position: absolute; right: 0; top: 110px;
    width: 150px; height: 70px; background: var(--blue);
  }
  .back-panel-red {
    position: absolute; right: 0; top: 185px;
    width: 150px; height: 115px; background: var(--red);
  }

  .holder { position: absolute; right: 40px; top: 40px; text-align: right; font-family: "Arimo", sans-serif; }
  .holder-name { color: var(--red); font-size: 20px; }
  .holder-title { color: var(--navy); font-size: 14px; margin-top: 2px; }

  .logo { position: absolute; left: 70px; top: 62px; display: flex; align-items: center; gap: 10px; }
  .logo-mark { width: 26px; height: 26px; background: var(--red); }
  .logo-name { font-family: "Source Sans 3", sans-serif; font-weight: 700; font-size: 44px; color: var(--navy); line-height: 1; }
  .back-company { position: absolute; left: 70px; top: 120px; font-size: 26px; }

  .contacts { position: absolute; left: 70px; top: 190px; list-style: none; font-family: "Arimo", sans-serif; color: var(--body); font-size: 19px; }
  .contacts li { display: flex; align-items: center; gap: 12px; height: 28px; white-space: nowrap; }
  .contacts svg { width: 16px; height: 16px; fill: var(--red); flex: none; }
</style>
</head>
<body>
<main class="stage">

  <section class="card card--front" aria-label="Card front">
    <div class="front-panel"></div>
    <div class="front-band-red"></div>
    <div class="front-band-blue"></div>
    <div class="front-edge"></div>
    <div class="front-brand">
      <p class="company">Redline Trade Ventures</p>
      <p class="website-line">www.<span class="accent">rtvtrade</span>.com</p>
    </div>
  </section>

  <section class="card card--back" aria-label="Card back">
    <div class="side-bar"><span class="seg-blue-top"></span><span class="seg-red"></span><span class="seg-blue-bottom"></span></div>
    <div class="back-panel-blue"></div>
    <div class="back-panel-red"></div>

    <div class="holder">
      <p class="holder-name">Marcus Hale</p>
      <p class="holder-title">Job Title</p>
    </div>

    <div class="logo">
      <span class="logo-mark"></span>
      <span class="logo-name">RTV</span>
    </div>
    <p class="company back-company">Redline Trade Ventures</p>

    <ul class="contacts">
      <li><svg viewBox="0 0 16 16" aria-hidden="true"><path d="M3 1l3 3-2 2c1 2 3 4 5 5l2-2 3 3-2 3C6 15 1 10 1 3z"/></svg>555.214.0187</li>
      <li><svg viewBox="0 0 16 16" aria-hidden="true"><path d="M4 0h8v16H4zM5.5 2v10h5V2zM7 13.5h2v1H7z" fill-rule="evenodd"/></svg>555.362.4470</li>
      <li><svg viewBox="0 0 16 16" aria-hidden="true"><path d="M4 1h8v4H4zM1 6h14v6h-3v3H4v-3H1zM5.5 10v3.5h5V10z" fill-rule="evenodd"/></svg>555.907.3182</li>
      <li><svg viewBox="0 0 16 16" aria-hidden="true"><path d="M1 3h14v10H1zM2 4.5v.5l6 4 6-4v-.5z" fill-rule="evenodd"/></svg>marcus@rtvtrade.com</li>
      <li><svg viewBox="0 0 16 16" aria-hidden="true"><circle cx="8" cy="8" r="7"/><path d="M8 1v14M1 8h14" stroke="#fff" stroke-width="1" fill="none"/></svg>www.rtvtrade.com</li>
      <li><svg viewBox="0 0 16 16" aria-hidden="true"><path d="M8 0a5.5 5.5 0 0 0-5.5 5.5C2.5 10 8 16 8 16s5.5-6 5.5-10.5A5.5 5.5 0 0 0 8 0zm0 3.5a2 2 0 1 1 0 4 2 2 0 0 1 0-4z" fill-rule="evenodd"/></svg>1420 Foundry Road, Dayton, OH 45402</li>
    </ul>
  </section>

</main>
</body>
</html>
```